Creative, professional looking and complex double exposure profile picture for my website

I need a double exposure effect on the lower half of the image (where the jacket is) going downwards. The lower half of the design should not be a clear cut, either faded away or in the shapes of the double exposure effect (like trees or waves). I would imagine something like an ocean with Orcas, or forest, or perhaps a silhouette of a wildlife photographer inside a forest. There can be quite a few ideas explored.

I have also got another idea which I will be attaching as well. It's to have design at the bottom and the top as well, bottom representing ocean (maybe like a split shot with Tide Warden boat on the sea with orcas underneath the water surface) and top earth (trees, mountains, birds - if you can include the Tui bird from the photo I have originally attached into the trees that would be great). The top is going to be only a very slight double exposure (perhaps around the edges) and going to be mostly behind me as a background. The bottom will be normal double exposure. Both will NOT have a clear cut but will rather dissolve naturally into the space. Sending through a few images as a concept idea only.

You are not required to use photos, art designs and illustrations of the photos and the scenes I have attached are welcome as well. They however can't be cartoonish, needs to still look pro and fit the overall look of my website.

Lastly the design should outstand a dark background of my website (www.lensbeyondtrails.example).

UPDATE: I am actually quite intrigued by the following design as well (https://assets.velmorastock.example/animated-pencil-sketch-fx-photoshop-add-on-QK7RZT). If someone can pull this off along with a transparent background so it blends nicely on my homepage then I will award extra points to that design.

Photography

Should not have
• Cartoonish, childish looks. Clear cut edges.

```html
<!DOCTYPE html>
<html lang="en">
<head>
<meta charset="utf-8">
<title>Tomas — Lens Beyond Trails</title>
<link href="https://fonts.googleapis.com/css2?family=Marcellus&family=Cormorant+Garamond:wght@400&display=swap" rel="stylesheet">
<style>
  :root {
    --page-bg: #ffffff;
    --band-bg: #212121;
    --heading: #f4f4f4;
    --body-text: #9b9b9b;
    --button-bg: #747474;
    --button-text: #f2f2f2;
    --tone-light: #a8a8a8;
    --tone-mid: #5e5e5e;
    --tone-deep: #3a3a3a;
  }
  html, body {
    margin: 0;
    padding: 0;
    width: 1200px;
    height: 1000px;
    overflow: hidden;
    background: var(--page-bg);
  }
  .canvas {
    position: relative;
    width: 1200px;
    height: 1000px;
  }
  .intro-band {
    position: absolute;
    left: 0;
    top: 289px;
    width: 1200px;
    height: 511px;
    background: var(--band-bg);
  }
  .greeting {
    position: absolute;
    left: 60px;
    top: 205px;
    width: 280px;
    margin: 0;
    text-align: center;
    font-family: "Marcellus", serif;
    font-weight: 400;
    font-size: 32px;
    line-height: 49px;
    color: var(--heading);
  }
  .portrait {
    position: absolute;
    left: 432px;
    top: 112px;
    width: 350px;
    height: 335px;
  }
  .bio {
    position: absolute;
    left: 851px;
    top: 118px;
    width: 300px;
    text-align: center;
  }
  .bio-text {
    margin: 0;
    font-family: "Cormorant Garamond", serif;
    font-size: 16.8px;
    line-height: 29.6px;
    color: var(--body-text);
  }
  .about-button {
    display: inline-block;
    margin-top: 58px;
    width: 91px;
    height: 42px;
    line-height: 42px;
    background: var(--button-bg);
    color: var(--button-text);
    font-family: "Marcellus", serif;
    font-size: 12.5px;
    letter-spacing: 3px;
    text-decoration: none;
    text-align: center;
  }
</style>
</head>
<body>
  <div class="canvas">
    <section class="intro-band">
      <h1 class="greeting">Hi, my name is Tomas</h1>

      <svg class="portrait" viewBox="0 0 350 335" role="img"
           aria-label="Black and white double exposure portrait of the photographer: a misty forest and mountains within his hair, and a ship and an orca on the sea within his jacket, the lower edge dissolving softly into the dark background">
        <defs>
          <linearGradient id="portrait-tones" x1="0" y1="0" x2="0" y2="1">
            <stop offset="0" stop-color="var(--tone-light)"/>
            <stop offset="0.3" stop-color="var(--tone-mid)"/>
            <stop offset="0.55" stop-color="var(--tone-deep)"/>
            <stop offset="0.78" stop-color="var(--tone-mid)"/>
            <stop offset="1" stop-color="#212121"/>
          </linearGradient>
          <filter id="soft-edge" x="-20%" y="-20%" width="140%" height="140%">
            <feGaussianBlur stdDeviation="14"/>
          </filter>
        </defs>
        <rect x="40" y="20" width="270" height="295" rx="110"
              fill="url(#portrait-tones)" filter="url(#soft-edge)"/>
      </svg>

      <div class="bio">
        <p class="bio-text">I am the owner and photographer behind Lens Beyond Trails and an Associate Producer on feature length documentary Pastures Unseen. I am based in New Zealand with a mission to create lasting positive impact on the planet.</p>
        <a class="about-button" href="#about">ABOUT</a>
      </div>
    </section>
  </div>
</body>
</html>
```